Brisk Meadow Builders needs a product brochure

We need a new flyer for our Patio Perch Lounge. Here is some of the copy your will need.
"Turn your back yard into the ultimate entertianment venue with the stunning Patio Perch Lounge!"
"Entertain family & friends in your very own back yard!"
"Available with or without solar and comes in a variety of colors"
"The Patio Perch Lounge measures 5' deep by 10' wide and is 9'-6" at it's highest point"
"Constructed with treated 4x4's, primed then painted with Thornby Calder best exterior paint for years of care free enjoyment. Also, Marlow Pendt Keystead shingles are dimensional, have a 25 year warranty and are rated for 150 mph winds!"
"TV Mount included. Shelves and TV are sold separately"
There also needs to be a box where we can add the price into later. The price can change from time to time due to material cost fluctuation.
Look and feel
Each slider illustrates characteristics of the customer's brand and the style your logo design should communicate.

```html
<!DOCTYPE html>
<html lang="en">
<head>
<meta charset="utf-8">
<title>Patio Perch Lounge – Brisk Meadow Builders</title>
<link rel="stylesheet" href="https://fonts.googleapis.com/css2?family=Open+Sans:wdth,wght@75..100,300..800&display=swap">
<style>
  :root {
    --paper: #ecedec;
    --green: #5a9e3e;
    --orange: #f6b12a;
    --charcoal: #2e3033;
    --ink: #2b2b2b;
    --white: #ffffff;
  }
  * { margin: 0; padding: 0; box-sizing: border-box; }
  html, body { width: 927px; height: 1200px; overflow: hidden; background: var(--paper); }
  .flyer { position: relative; width: 927px; height: 1200px; background: var(--paper); font-family: "Open Sans", sans-serif; color: var(--ink); }
  .shapes { position: absolute; inset: 0; }
  .brand { position: absolute; left: 45px; top: 66px; display: flex; align-items: center; gap: 8px; font-weight: 700; font-stretch: 75%; font-size: 26px; color: var(--green); line-height: 1; }
  .brand-mark { width: 16px; height: 16px; background: var(--orange); }
  .about { position: absolute; left: 680px; top: 50px; width: 162px; text-align: center; font-size: 13px; line-height: 23px; color: var(--ink); }
  .price { position: absolute; left: 636px; top: 105px; width: 291px; height: 42px; display: flex; align-items: center; padding-left: 24px; font-weight: 700; font-stretch: 75%; font-size: 37px; color: var(--charcoal); }
  .headline { position: absolute; right: 47px; top: 184px; text-align: right; font-weight: 700; font-stretch: 75%; font-size: 40px; line-height: 54px; color: var(--white); }
  .features { position: absolute; left: 49px; top: 660px; list-style: none; font-weight: 600; font-stretch: 75%; font-size: 20px; line-height: 37.5px; color: var(--ink); }
  .dimensions { position: absolute; left: 463px; top: 960px; font-weight: 600; font-stretch: 75%; font-size: 20px; line-height: 31px; color: var(--white); }
  .construction { position: absolute; left: 50px; top: 1058px; width: 380px; font-size: 14.2px; line-height: 23.5px; color: var(--ink); }
  .call { position: absolute; left: 463px; top: 1091px; font-size: 26px; font-weight: 400; color: var(--charcoal); line-height: 1; }
  .phone { position: absolute; left: 462px; top: 1128px; font-weight: 700; font-stretch: 75%; font-size: 45px; color: var(--charcoal); line-height: 1; }
  .contact { position: absolute; left: 724px; top: 1088px; list-style: none; font-size: 14px; color: var(--charcoal); }
  .contact li { position: absolute; left: 0; white-space: nowrap; }
</style>
</head>
<body>
<main class="flyer">
  <svg class="shapes" width="927" height="1200" viewBox="0 0 927 1200">
    <defs>
      <linearGradient id="hero-tone" x1="0" y1="0" x2="0" y2="1">
        <stop offset="0" stop-color="#8fa85a"/>
        <stop offset="0.45" stop-color="#6a6458"/>
        <stop offset="1" stop-color="#8d8c90"/>
      </linearGradient>
      <linearGradient id="wood-tone" x1="0" y1="0" x2="1" y2="1">
        <stop offset="0" stop-color="#9a6a3a"/>
        <stop offset="1" stop-color="#3a3a3c"/>
      </linearGradient>
      <linearGradient id="scene-tone" x1="0" y1="0" x2="0" y2="1">
        <stop offset="0" stop-color="#7d9a55"/>
        <stop offset="0.5" stop-color="#4a4744"/>
        <stop offset="1" stop-color="#9a9a9e"/>
      </linearGradient>
    </defs>

    <polygon class="hero-photo" role="img" aria-label="Photo of the Patio Perch Lounge outdoor bar with solar panel roof, TV and guests seated at the counter on a stone patio" points="0,160 587,160 533,648 0,648" fill="url(#hero-tone)"/>
    <polygon class="hero-divider" points="587,160 609,160 554,648 533,648" fill="var(--charcoal)"/>
    <polygon class="hero-panel" points="609,160 927,160 927,648 554,648" fill="var(--green)"/>

    <rect class="detail-photo" role="img" aria-label="Photo of the wall-mounted bottle shelf with glasses" x="605" y="655" width="183" height="129" fill="url(#wood-tone)"/>
    <rect class="detail-photo" role="img" aria-label="Photo of a bartender serving a guest at the counter" x="509" y="785" width="184" height="138" fill="url(#scene-tone)"/>
    <rect class="detail-photo" role="img" aria-label="Photo of the wooden counter with a cup holder ledge" x="698" y="782" width="184" height="138" fill="url(#wood-tone)"/>

    <rect class="frame" x="43.5" y="775.5" width="343" height="260" fill="none" stroke="var(--green)" stroke-width="1.2"/>
    <rect class="front-photo" role="img" aria-label="Front view photo of the Patio Perch Lounge with three bar stools and a grill beside it" x="50" y="781" width="331" height="248" fill="url(#scene-tone)"/>

    <polygon class="dimension-band" points="425,948 927,948 927,1036 436,1036" fill="var(--green)"/>
    <polygon class="contact-box" points="440,1055 927,1055 927,1200 421,1200" fill="var(--orange)"/>
  </svg>

  <div class="brand"><span class="brand-mark"></span>Brisk Meadow Builders</div>
  <p class="about">About Brisk Meadow<br>Builders</p>
  <div class="price">$ 000,000.00</div>

  <h1 class="headline">Turn your<br>back yard into<br>the ultimate<br>entertainment<br>venue with<br>the stunning<br>Patio Perch<br>Lounge!</h1>

  <ul class="features">
    <li>Entertain family &amp; friends in your very own back yard!</li>
    <li>Available with or without solar and comes in a variety of colors</li>
    <li>TV Mount included. Shelves and TV are sold separately</li>
  </ul>

  <p class="dimensions">The Patio Perch Lounge measures 5' deep by 10' wide<br>and is 9'-6" at it's highest point</p>

  <p class="construction">Constructed with treated 4x4's, primed then painted with Thornby Calder best exterior paint for years of care free enjoyment. Also, Marlow Pendt Keystead shingles are dimensional, have a 25 year warranty and are rated for 150 mph winds!</p>

  <p class="call">CALL FOR US</p>
  <p class="phone">(000) 000-0000</p>
  <ul class="contact">
    <li style="top:0">Address:</li>
    <li style="top:42px">Email:</li>
    <li style="top:70px">Web:</li>
  </ul>
</main>
</body>
</html>
```